Brightpath Wellness biz card design
Northvale Medica Business Card
Brightpath Wellness biz card design - Health
Creative Brief
Use specific fonts
I dont care about font as long as it looks good
Modern
Derek T. L. Branwell
Chief Development Officer
4870 Harlow Ave Mailstop 3 Nashville TN 37211
derek.branwell@northvalemedicallc.example
We want the front to be a portfolio view. Something neat and creative.
Please use a creative variation of the logo.

```html
<!DOCTYPE html>
<html lang="en">
<head>
<meta charset="utf-8">
<title>Northvale Medica Business Card</title>
<link href="https://fonts.googleapis.com/css2?family=Raleway:wght@400;500;700;800&display=swap" rel="stylesheet">
<style>
  :root {
    --page-bg: #e9e6e2;
    --card-bg: #ffffff;
    --brand-blue: #1f86d0;
    --brand-green: #7dc242;
    --text-grey: #5a5f66;
    --text-soft: #8a9098;
  }
  html, body {
    margin: 0;
    padding: 0;
    width: 1200px;
    height: 914px;
    overflow: hidden;
    background: var(--page-bg);
    font-family: "Raleway", Arial, sans-serif;
  }
  .business-card {
    position: absolute;
    left: 80px;
    top: 137px;
    width: 1040px;
    height: 640px;
    background: var(--card-bg);
    box-shadow: 0 18px 40px rgba(0,0,0,0.18);
    overflow: hidden;
  }
  .card-swoosh {
    position: absolute;
    inset: 0;
    width: 1040px;
    height: 640px;
  }
  .brand {
    position: absolute;
    left: 72px;
    top: 92px;
  }
  .brand-lockup {
    display: flex;
    align-items: center;
    gap: 16px;
  }
  .brand-dot {
    width: 52px;
    height: 52px;
    border-radius: 50%;
    background: var(--brand-green);
  }
  .brand-name {
    font-size: 54px;
    font-weight: 800;
    color: var(--brand-blue);
    letter-spacing: -0.5px;
    line-height: 1;
  }
  .brand-tagline {
    margin: 14px 0 0 70px;
    font-size: 19px;
    font-weight: 500;
    color: var(--text-soft);
  }
  .contact-block {
    position: absolute;
    left: 72px;
    top: 262px;
    color: var(--text-grey);
    font-size: 20px;
    line-height: 1.45;
  }
  .contact-address {
    margin: 0 0 10px;
  }
  .contact-list {
    list-style: none;
    margin: 0;
    padding: 0;
  }
  .contact-item {
    display: flex;
    align-items: center;
    gap: 12px;
    margin-bottom: 4px;
  }
  .contact-icon {
    width: 22px;
    height: 22px;
    flex: none;
  }
  .person {
    position: absolute;
    right: 64px;
    bottom: 62px;
    text-align: right;
  }
  .person-name {
    margin: 0;
    font-size: 24px;
    font-weight: 700;
    color: var(--brand-blue);
  }
  .person-title {
    margin: 4px 0 0;
    font-size: 21px;
    font-weight: 500;
    color: var(--brand-green);
  }
</style>
</head>
<body>
  <main class="business-card">
    <svg class="card-swoosh" viewBox="0 0 1040 640" aria-hidden="true">
      <path d="M640,0 L1040,0 L1040,300 C930,190 800,80 640,0 Z" fill="var(--brand-blue)"/>
      <path d="M615,0 L640,0 C800,80 930,190 1040,300 L1040,330 C920,210 780,90 615,0 Z" fill="#ffffff"/>
      <path d="M585,0 L615,0 C780,90 920,210 1040,330 L1040,364 C910,235 760,100 585,0 Z" fill="var(--brand-green)"/>
      <path d="M720,0 L765,0 C875,70 965,145 1040,215 L1040,250 C955,170 850,85 720,0 Z" fill="var(--brand-green)" opacity="0.85"/>
    </svg>

    <header class="brand">
      <div class="brand-lockup">
        <span class="brand-dot"></span>
        <span class="brand-name">Northvale Medica</span>
      </div>
      <p class="brand-tagline">Expert care for senior facilities</p>
    </header>

    <section class="contact-block">
      <p class="contact-address">4870 Harlow Ave Mailstop 3 Nashville<br>TN 37211</p>
      <ul class="contact-list">
        <li class="contact-item">
          <svg class="contact-icon" viewBox="0 0 22 22" aria-hidden="true">
            <circle cx="11" cy="11" r="11" fill="var(--brand-blue)"/>
            <path d="M7.5,6 L9.3,6 L10,8.6 L8.9,9.5 C9.6,11 10.9,12.3 12.4,13 L13.3,11.9 L15.9,12.6 L15.9,14.4 C15.9,15 15.4,15.5 14.8,15.4 C10.2,15 6.9,11.7 6.5,7.1 C6.5,6.5 6.9,6 7.5,6 Z" fill="#fff"/>
          </svg>
          <span>615-555-0148</span>
        </li>
        <li class="contact-item">
          <svg class="contact-icon" viewBox="0 0 22 22" aria-hidden="true">
            <circle cx="11" cy="11" r="11" fill="var(--brand-blue)"/>
            <rect x="5.5" y="7" width="11" height="8" rx="1" fill="#fff"/>
            <path d="M5.8,7.4 L11,11.4 L16.2,7.4" stroke="var(--brand-blue)" stroke-width="1.2" fill="none"/>
          </svg>
          <span>derek.branwell@northvalemedicallc.example</span>
        </li>
        <li class="contact-item">
          <svg class="contact-icon" viewBox="0 0 22 22" aria-hidden="true">
            <circle cx="11" cy="11" r="11" fill="var(--brand-blue)"/>
            <circle cx="11" cy="11" r="5.5" stroke="#fff" stroke-width="1.3" fill="none"/>
            <ellipse cx="11" cy="11" rx="2.3" ry="5.5" stroke="#fff" stroke-width="1.1" fill="none"/>
            <line x1="5.5" y1="11" x2="16.5" y2="11" stroke="#fff" stroke-width="1.1"/>
          </svg>
          <span>www.northvalemedicallc.example</span>
        </li>
      </ul>
    </section>

    <footer class="person">
      <p class="person-name">Derek T. L. Branwell</p>
      <p class="person-title">Chief Development Officer</p>
    </footer>
  </main>
</body>
</html>
```